Business Card Design for Photographer

Updating business card design. Must use included logo. We're a luxury wedding photography business. Elegancy, luxury, consistency are messages we wish to convey.

Visit our website at www.colvanderose.com to familiarize yourself more with our brand design currently (fonts, colors etc.). This is what we want to maintain.

Target Market(s)

Luxury Brides and Grooms

Industry/Entity Type

Wedding

Contact Information for Business Card

Current logo (attached to brief)
Name: Colin Vanderose
Phone: 5871302948
website/blog
Email

Requirements
Must have
• Current logo (attached to brief)
• Name: Colin Vanderose
• Phone: 5871302948
• website/blog
• Email
• Instagram username
Should not have
• bright colors, fonts that don't suit our brand (visit www.colvanderose.com)

```html
<!DOCTYPE html>
<html lang="en">
<head>
<meta charset="utf-8">
<title>Colin Vanderose Photographers – Business Card</title>
<link rel="stylesheet" href="https://fonts.googleapis.com/css2?family=Josefin+Sans:wght@300;400&family=EB+Garamond:ital,wght@1,400;1,600&display=swap">
<style>
  :root {
    --backdrop: #e9e6e1;
    --card: #fbfbfa;
    --card-edge: #e2e2e0;
    --ink: #8a8a8a;
    --ink-dark: #6f6f6f;
    --ink-soft: #a3a3a3;
    --block-light: #9d9d9d;
    --block-dark: #7b7b7b;
    --shadow: rgba(60, 50, 40, 0.22);
  }
  * { margin: 0; padding: 0; box-sizing: border-box; }
  html, body {
    width: 1200px;
    height: 1023px;
    overflow: hidden;
    background: var(--backdrop);
  }
  .stage { position: relative; width: 1200px; height: 1023px; }

  .card {
    position: absolute;
    width: 560px;
    height: 320px;
    background: var(--card);
    box-shadow: 0 2px 0 var(--card-edge), 0 4px 0 #d6d6d4, 0 18px 36px var(--shadow);
    overflow: hidden;
  }

  /* Front */
  .card-front { left: 80px; top: 120px; }
  .brand {
    position: absolute;
    left: 0; right: 0; top: 92px;
    display: flex; flex-direction: column; align-items: center;
  }
  .brand-mark {
    width: 38px; height: 38px;
    background: var(--ink-soft);
    margin-bottom: 22px;
  }
  .brand-name {
    font-family: "Josefin Sans", sans-serif;
    font-weight: 300;
    font-size: 27px;
    letter-spacing: 0.26em;
    color: var(--ink);
    text-transform: uppercase;
    padding-left: 0.26em;
  }
  .brand-tagline {
    margin-top: 8px;
    font-family: "Josefin Sans", sans-serif;
    font-weight: 300;
    font-size: 13px;
    letter-spacing: 0.62em;
    color: var(--ink);
    text-transform: uppercase;
    padding-left: 0.62em;
  }

  /* Back */
  .card-back { left: 560px; top: 600px; }
  .monogram-block {
    position: absolute;
    left: 0; top: 0;
    width: 300px; height: 250px;
    background: linear-gradient(160deg, var(--block-light), var(--block-dark));
  }
  .contact {
    position: absolute;
    right: 34px; top: 150px;
    text-align: right;
    font-family: "EB Garamond", serif;
    font-style: italic;
    color: var(--ink);
  }
  .contact-name {
    font-weight: 600;
    font-size: 22px;
    color: var(--ink-dark);
    margin-bottom: 8px;
  }
  .contact-line {
    font-size: 15px;
    letter-spacing: 0.14em;
    line-height: 1.35;
  }
  .social {
    position: absolute;
    left: 22px; bottom: 22px;
    display: flex; align-items: center; gap: 9px;
    font-family: "EB Garamond", serif;
    font-style: italic;
    font-size: 14px;
    letter-spacing: 0.16em;
    color: var(--ink-soft);
  }
  .social-square {
    width: 12px; height: 12px;
    border: 1.5px solid var(--ink-soft);
  }
</style>
</head>
<body>
<main class="stage">
  <section class="card card-front" aria-label="Business card front">
    <div class="brand">
      <div class="brand-mark"></div>
      <div class="brand-name">Colin Vanderose</div>
      <div class="brand-tagline">Photographers</div>
    </div>
  </section>

  <section class="card card-back" aria-label="Business card back">
    <div class="monogram-block" role="img" aria-label="Large grey brand monogram area"></div>
    <div class="contact">
      <div class="contact-name">Colin Vanderose</div>
      <div class="contact-line">(587) 130-2948</div>
      <div class="contact-line">colin@colvanderose.com</div>
      <div class="contact-line">www.colvanderose.com</div>
    </div>
    <div class="social">
      <span class="social-square"></span>
      <span>colvanderosephoto</span>
    </div>
  </section>
</main>
</body>
</html>
```